Homepage for the brisk-trail Web Application

At the end of this text, you will find a link to a website that is under construction for a webApp that I intend to launch soon. The contest goal is for you to make redesign the homepage in a nice, fresh, modern Style. Only design, no coding necessary. It needs to have a responsive version for small screens like smart phones. Attached is the text for it, and some images that you may use. You are welcome to find or create additional supporting images. You can use PixVaultimages.com or similar service to find new images as long as I can purchase the non-exclusive use rights for the images at similar prices. The contest is just for the home page. However, the winner, if I like the work and we can agree on a fair price, could be contracted on a one-on-one basis to do the rest of the site. You are welcome to suggest minor changes like font sizes and minor variations on the Header banner, but that banner is consistent with the user interface of the application therefore should not change too much. The information should flow somewhat continually without much use of side bars or things like that.
https://www.brisk-trail-example.com
Sincerely,
Marco R. Delgado

```html
<!DOCTYPE html>
<html lang="en">
<head>
<meta charset="utf-8">
<title>Brisk Trail – Home</title>
<link href="https://fonts.googleapis.com/css2?family=Montserrat:ital,wght@0,300;0,400;0,500;0,600;0,700;0,800;1,300&family=Open+Sans:wght@400;600;700&display=swap" rel="stylesheet">
<style>
:root{
  --orange:#f5794f;
  --blue:#1b7ec6;
  --teal:#46d3d6;
  --ink:#1d1d1d;
  --muted:#666;
  --footer:#1f1f1f;
  --footer-bar:#333;
  --footer-text:#dddddd;
  --white:#fff;
  --card:#f3f3f3;
}
*{box-sizing:border-box;margin:0;padding:0}
html,body{width:1200px;height:4847px;overflow:hidden}
body{position:relative;font-family:"Open Sans",Arial,sans-serif;color:var(--ink);background:var(--white)}
.abs{position:absolute}
.center{text-align:center;left:0;width:1200px}
.eyebrow{font-family:"Montserrat",sans-serif;font-weight:600;font-size:11px;letter-spacing:.3px;text-transform:uppercase}
.h2{font-family:"Montserrat",sans-serif;font-weight:600;font-size:31px}
.pill{position:absolute;display:flex;align-items:center;justify-content:center;border-radius:20px;font-family:"Montserrat",sans-serif;font-weight:700;font-size:10px;text-transform:uppercase;color:#fff;background:var(--orange)}

/* header */
.top-line{top:0;left:0;width:1200px;height:7px;background:var(--orange)}
.site-header{top:7px;left:0;width:1200px;height:123px;background:#fff}
.brand{left:76px;top:44px;display:flex;align-items:center;gap:10px;font-family:"Montserrat",sans-serif;font-weight:600;font-size:42px;color:var(--orange)}
.brand-dot{width:28px;height:28px;border-radius:50%;background:var(--teal)}
.contact-line{left:742px;top:39px;font-size:11px;color:var(--muted)}
.contact-line b{color:var(--orange);font-weight:600}
.login{left:1062px;top:39px;font-size:11px;color:var(--muted);display:flex;gap:6px;align-items:center}
.main-nav{left:526px;top:76px;display:flex;gap:26px;font-size:11.5px;color:var(--blue)}
.trial-btn{left:1036px;top:68px;width:105px;height:31px;font-size:12px;text-transform:none}

/* hero */
.hero{top:130px;left:0;width:1200px;height:543px;background:linear-gradient(120deg,#1f8fd3 0%,#2178c6 60%,#1f6ec0 100%)}
.hero-art{left:75px;top:160px;width:490px;height:550px;border-radius:30px;background:linear-gradient(160deg,#7fe3e6 0%,#3fc3c9 55%,#f08a63 100%);opacity:.9}
.hero-copy{left:598px;top:278px;font-family:"Montserrat",sans-serif;line-height:1;white-space:nowrap}
.hero-copy .l1{font-style:italic;font-weight:300;font-size:40px;color:var(--teal)}
.hero-copy .l2{font-weight:800;font-size:49px;color:#fff;margin-top:6px}
.hero-copy .l3{font-weight:800;font-size:45px;color:#fff}
.hero-copy .l4{font-weight:300;font-size:49px;color:var(--teal);margin-top:2px}
.btn-hero{position:absolute;top:489px;height:50px;border-radius:8px;display:flex;align-items:center;justify-content:center;font-family:"Montserrat",sans-serif;font-size:20px;color:#fff}
.btn-hero.solid{left:610px;width:177px;background:var(--orange)}
.btn-hero.ghost{left:813px;width:208px;border:2px solid #fff}

/* welcome */
.welcome-eyebrow{top:791px;color:var(--orange)}
.welcome-title{top:812px;font-size:32px}
.welcome-text{left:107px;top:888px;width:986px;font-size:11.5px;line-height:14px;color:#444}
.welcome-btn{left:544px;top:988px;width:113px;height:37px}

/* pricing */
.pricing{top:1102px;left:0;width:1200px;height:709px;background:linear-gradient(115deg,#1a6fc2 0%,#1f8ad0 50%,#2aa8e0 100%)}
.pricing-eyebrow{top:1192px;color:#fff;text-transform:none;font-size:10px}
.pricing-title{top:1210px;color:#fff}
.pricing-sub{top:1252px;left:410px;width:380px;text-align:center;color:#e6f2fb;font-size:11px;line-height:15px}
.plan{position:absolute;width:244px;text-align:center;background:var(--card);font-family:"Montserrat",sans-serif}
.plan .name{position:absolute;left:0;width:100%;font-weight:600;font-size:12px}
.plan .price{position:absolute;left:0;width:100%;font-weight:600;font-size:58px;color:var(--blue)}
.plan .price sup{font-size:28px;vertical-align:-14px;margin-right:2px}
.plan .desc{position:absolute;left:40px;width:164px;font-size:10px;line-height:14px;font-weight:600;color:#444}
.plan .pill{left:64px;width:117px;height:34px}
.plan.starter{left:209px;top:1343px;height:335px}
.plan.advance{left:745px;top:1343px;height:335px}
.plan.basic{left:478px;top:1317px;height:365px;background:var(--orange);color:#fff}
.plan.basic .price,.plan.basic .desc,.plan.basic .name{color:#fff}
.plan.basic .pill{background:#fff;color:var(--orange)}

/* blog */
.blog-eyebrow{top:1895px;color:var(--blue)}
.blog-title{top:1912px;font-size:28px}
.blog-sub{top:1954px;left:395px;width:410px;text-align:center;font-size:11px;line-height:14px;color:#555}
.post{position:absolute;top:2031px;width:284px}
.post .photo{width:284px;height:189px}
.post .meta{margin:22px 0 0 17px;font-size:9.5px;color:#333}
.post .title{margin:16px 0 0 17px;font-family:"Montserrat",sans-serif;font-weight:600;font-size:15.5px;line-height:19px;color:var(--orange)}
.post .excerpt{margin:14px 0 0 17px;width:240px;font-size:9.5px;line-height:13px;color:#777}
.post .pill{position:relative;margin:12px 0 0 14px;width:115px;height:28px;font-size:9px}

/* testimonials */
.reviews{top:2517px;left:0;width:1200px;height:402px;background:linear-gradient(110deg,#1b66bb 0%,#1f8fd3 60%,#27a7df 100%)}
.reviews-eyebrow{top:2578px;color:#fff;font-size:10px}
.reviews-title{top:2592px;color:#fff;font-size:28px}
.review{position:absolute;top:2679px;width:309px;height:129px;border:2px solid #fff;padding:22px 22px 0}
.review .mark{position:absolute;left:20px;top:-26px;font-family:Georgia,serif;font-weight:700;font-size:48px;line-height:1;color:#fff;background:#1f7fca;padding:0 4px}
.review .head{font-family:"Montserrat",sans-serif;font-weight:600;font-size:12.5px;color:#fff}
.review .body{margin-top:6px;font-size:10px;line-height:15px;color:#eaf4fc;text-align:justify}
.review .who{position:absolute;left:31px;top:144px;font-family:"Montserrat",sans-serif;font-weight:600;font-size:12.5px;color:#fff;text-transform:uppercase}
.review .role{position:absolute;left:31px;top:161px;font-size:10px;color:#e6f2fb}
.arrow{position:absolute;top:2712px}

/* contact */
.contact-bg{top:2919px;left:0;width:1200px;height:623px;background:linear-gradient(90deg,#dff7f7 0%,#f7fdfd 40%,#fbefe9 75%,#f6b6a0 100%)}
.contact-card{left:233px;top:3004px;width:758px;height:470px;background:#fff;box-shadow:0 6px 24px rgba(0,0,0,.08)}
.contact-eyebrow{top:3047px;color:#333;font-weight:500}
.contact-title{top:3064px;font-size:28px}
.contact-sub{top:3112px;left:350px;width:500px;text-align:center;font-size:11px;line-height:15px;color:#777}
.field{position:absolute;left:267px;width:334px;height:36px;border:1.5px solid #ddd;border-radius:18px;padding:0 16px;display:flex;align-items:center;font-size:11px;color:#888}
.field.comment{left:624px;top:3224px;width:335px;height:146px;align-items:flex-start;padding-top:14px}
.send-btn{left:813px;top:3405px;width:146px;height:34px}

/* download */
.download{top:3542px;left:0;width:1200px;height:376px;background:var(--orange)}
.download-eyebrow{top:3637px;color:#fff;font-size:10px}
.download-title{top:3652px;color:#fff;font-size:30px}
.download-text{top:3717px;left:220px;width:760px;text-align:center;font-size:11px;line-height:15px;color:#fff}
.store{position:absolute;top:3811px;height:40px;border:2px solid #fff;border-radius:20px;display:flex;align-items:center;justify-content:center;gap:8px;font-family:"Montserrat",sans-serif;font-weight:600;font-size:10.5px;color:#fff;text-transform:uppercase}
.store i{width:12px;height:12px;border-radius:50%;background:#fff;display:block}

/* faq */
.faq-title{top:4018px;font-family:"Montserrat",sans-serif;font-weight:700;font-size:28px}
.faq-sub{top:4056px;color:var(--blue)}
.faq-item{position:absolute;left:130px;width:377px;height:46px;border:1.5px solid var(--blue);display:flex;align-items:center;justify-content:space-between;padding:0 12px 0 24px;font-size:10.5px;color:#333;text-transform:uppercase}
.faq-item .plus{font-size:22px;color:var(--blue)}
.faq-open{left:549px;top:4144px;width:520px;height:256px;background:var(--blue);padding:36px 32px 0 34px;color:#fff}
.faq-open .q{font-size:11px;text-transform:uppercase;display:flex;justify-content:space-between}
.faq-open .a{margin-top:14px;font-size:10px;line-height:15px;text-align:justify;color:#eaf3fb}

/* footer */
.site-footer{top:4499px;left:0;width:1200px;height:288px;background:var(--footer)}
.foot-brand{left:113px;top:4558px;display:flex;align-items:center;gap:8px;font-family:"Montserrat",sans-serif;font-weight:600;font-size:32px;color:var(--orange)}
.foot-brand .brand-dot{width:20px;height:20px}
.foot-about{left:111px;top:4624px;width:200px;font-size:11.5px;line-height:16px;color:var(--footer-text)}
.socials{left:111px;top:4716px;display:flex;gap:6px}
.socials i{width:17px;height:17px;border-radius:50%;background:var(--orange);display:block}
.foot-h{font-family:"Montserrat",sans-serif;font-weight:600;font-size:15px;color:var(--orange)}
.foot-col{font-size:12px;line-height:17px;color:var(--footer-text)}
.quick-links{left:668px;top:4603px;list-style:none;font-size:12.5px;line-height:23.5px;color:var(--footer-text)}
.quick-links li::before{content:"";display:inline-block;border-left:5px solid var(--orange);border-top:4px solid transparent;border-bottom:4px solid transparent;margin-right:10px}
.practice{left:929px;top:4603px;list-style:none;font-size:12.5px;color:var(--footer-text)}
.practice li{width:156px;padding:3px 0 4px;border-bottom:1px solid #ccc;margin-bottom:1px}
.copyright{top:4787px;left:0;width:1200px;height:60px;background:var(--footer-bar);color:#ccc;font-size:11.5px;display:flex;align-items:center;justify-content:center}
</style>
</head>
<body>

<!-- Header -->
<div class="abs top-line"></div>
<header class="abs site-header"></header>
<div class="abs brand"><span class="brand-dot"></span>Brisk Trail</div>
<div class="abs contact-line"><b>Call Us</b> 555.010.2020 &nbsp; <b>Email :</b> hello@brisktrail.example</div>
<div class="abs login">Login
  <svg width="16" height="18" viewBox="0 0 16 18" fill="none" stroke="#f5794f" stroke-width="1.4"><circle cx="8" cy="5" r="4"/><path d="M1 17c0-4 3-6 7-6s7 2 7 6"/></svg>
</div>
<nav class="abs main-nav"><span>Home</span><span>About us</span><span>Pricing</span><span>Blog</span><span>FAQS</span><span>Support</span><span>Reviews</span><span>Contact us</span></nav>
<div class="pill trial-btn">Free - Trail</div>

<!-- Hero -->
<section class="abs hero"></section>
<div class="abs hero-art" role="img" aria-label="Isometric illustration of a man filing folders into a drawer cabinet standing on a laptop"></div>
<div class="abs hero-copy">
  <div class="l1">Keeping track of all your</div>
  <div class="l2">PAPER DOCUMENTS</div>
  <div class="l3">&amp; OTHER BELONGINGS</div>
  <div class="l4">has never been easier!</div>
</div>
<div class="btn-hero solid">Free Trial</div>
<div class="btn-hero ghost">Download App</div>

<!-- Welcome -->
<div class="abs center eyebrow welcome-eyebrow">Find any document or item instantly!</div>
<h1 class="abs center h2 welcome-title">Welcome to Brisk Trail</h1>
<p class="abs welcome-text">Brisk-Trail is a system that allows you to quickly search for the location of every item that you store or file. It is an essential tool for keeping track of paper documents or any other kind of physical item. You'll have the ability to quickly find any item you're searching for, even years after you've stored it. More importantly, using Brisk-Trail helps you save considerable space without losing speedy accessibility to your treasured items.</p>
<div class="pill welcome-btn">Read more</div>

<!-- Pricing -->
<section class="abs pricing"></section>
<div class="abs center eyebrow pricing-eyebrow">Get Started Now</div>
<h2 class="abs center h2 pricing-title">Our Pricing Plans</h2>
<p class="abs pricing-sub">Lorem ipsum dolor sit amet, consectetur adipiscing elit. Quid autem habent admirationis, cum prope accesseris</p>

<div class="plan starter">
  <div class="name" style="top:44px">STARTER PLAN</div>
  <div class="price" style="top:98px"><sup>$</sup>125</div>
  <div class="desc" style="top:197px">Lorem ipsum dolor sit amet, consectetur adipisc aliter in vita</div>
  <div class="pill" style="top:270px">Get Starter</div>
</div>
<div class="plan basic">
  <div class="name" style="top:64px">BASIC PLAN</div>
  <div class="price" style="top:126px"><sup>$</sup>165</div>
  <div class="desc" style="top:225px">Lorem ipsum dolor sit amet, consectetur adipisc aliter in vita</div>
  <div class="pill" style="top:297px">Get Starter</div>
</div>
<div class="plan advance">
  <div class="name" style="top:44px">ADVANCE PLAN</div>
  <div class="price" style="top:100px"><sup>$</sup>195</div>
  <div class="desc" style="top:199px">Lorem ipsum dolor sit amet, consectetur adipisc aliter in vita</div>
  <div class="pill" style="top:273px">Get Starter</div>
</div>

<!-- Blog -->
<div class="abs center eyebrow blog-eyebrow">Ostrud an est</div>
<h2 class="abs center h2 blog-title">Lates Blog</h2>
<p class="abs blog-sub">Lorem ipsum dolor sit amet, cu per porro dolore nostro, partem cu per porro integre corpora per ea, tation ornatus mel ad</p>

<article class="post" style="left:143px">
  <div class="photo" role="img" aria-label="Photo of a hand holding a smartphone beside a coffee cup and keyboard" style="background:linear-gradient(135deg,#d9d6d1,#8a8580 60%,#3b3a38)"></div>
  <div class="meta">By Admin | 4 January 2021</div>
  <div class="title">Lorem ipsum dolor sit amet cu per porro dolore nostro</div>
  <div class="excerpt">Lorem ipsum dolor sit amet, cu per porro dolore nostro, partem integre corpora per ea, tation ornatus mel ad Brute voluptatibus an</div>
  <div class="pill">Read more</div>
</article>
<article class="post" style="left:450px">
  <div class="photo" role="img" aria-label="Photo of two colleagues looking at a computer screen in a dim office" style="background:linear-gradient(135deg,#4a5158,#2a2f35 55%,#8fa0ae)"></div>
  <div class="meta">By Admin | 4 January 2021</div>
  <div class="title">Sum dolor sit amet cu per porro dolore nostro</div>
  <div class="excerpt">Lorem ipsum dolor sit amet, cu per porro dolore nostro, partem integre corpora per ea, tation ornatus mel ad Brute voluptatibus an</div>
  <div class="pill">Read more</div>
</article>
<article class="post" style="left:756px">
  <div class="photo" role="img" aria-label="Photo of a smiling woman using her phone by a sunny window" style="background:linear-gradient(135deg,#f2c33b,#d89a2a 50%,#5a3a22)"></div>
  <div class="meta">By Admin | 4 January 2021</div>
  <div class="title">Porro dolore nostro Lorem ipsum dolor sit ametcu per</div>
  <div class="excerpt">Lorem ipsum dolor sit amet, cu per porro dolore nostro, partem integre corpora per ea, tation ornatus mel ad Brute voluptatibus an</div>
  <div class="pill">Read more</div>
</article>

<!-- Testimonials -->
<section class="abs reviews"></section>
<div class="abs center eyebrow reviews-eyebrow">Testimonial</div>
<h2 class="abs center h2 reviews-title">Customers Reviews</h2>
<svg class="arrow" style="left:142px" width="32" height="60" viewBox="0 0 32 60" fill="none" stroke="#fff" stroke-width="2.5"><path d="M29 2 3 30l26 28"/></svg>
<svg class="arrow" style="left:1024px" width="32" height="60" viewBox="0 0 32 60" fill="none" stroke="#fff" stroke-width="2.5"><path d="M3 2l26 28L3 58"/></svg>
<div class="review" style="left:260px">
  <span class="mark">“</span>
  <div class="head">Highly Professional Team</div>
  <div class="body">Lorem ipsum dolor sit amet, consectetur adipiscing elit. Quid autem habent admirationis, cum prope accesseris? An hoc usque quaque, aliter in vita?</div>
  <div class="who">Harlan Brooks</div>
  <div class="role">Manager</div>
</div>
<div class="review" style="left:630px">
  <span class="mark">“</span>
  <div class="head">Highly Professional Team</div>
  <div class="body">Lorem ipsum dolor sit amet, consectetur adipiscing elit. Quid autem habent admirationis, cum prope accesseris? An hoc usque quaque, aliter in vita?</div>
  <div class="who">Dorian Webb</div>
  <div class="role">Top Manager</div>
</div>

<!-- Contact -->
<section class="abs contact-bg" role="img" aria-label="Soft decorative illustration of a pale teal device on the left and a coral shape on the right"></section>
<div class="abs contact-card"></div>
<div class="abs center eyebrow contact-eyebrow">Contact</div>
<h2 class="abs center h2 contact-title">Get in Touch</h2>
<p class="abs contact-sub">Lorem ipsum dolor sit amet, consectetur adipiscing elit. Quid autem habent admirationis, Non igitur de improbo, sed de callido improbo quaerimus, qualis</p>
<div class="field" style="top:3224px">Name*</div>
<div class="field" style="top:3279px">Email*</div>
<div class="field" style="top:3333px">Phone*</div>
<div class="field comment">Comment*</div>
<div class="pill send-btn">Send Message</div>

<!-- Download -->
<section class="abs download"></section>
<div class="abs center eyebrow download-eyebrow">Autem habent</div>
<h2 class="abs center h2 download-title">Download App</h2>
<p class="abs download-text">Lorem ipsum dolor sit amet, consectetur adipiscing elit. Quid autem habent admirationis, cum prope accesseris? An hoc usque quaque, aliter in vita cum propequaque, aliter in vita? An hoc usqu</p>
<div class="store" style="left:337px;width:144px"><i></i>Phone Store</div>
<div class="store" style="left:498px;width:157px"><i></i>Tablet Store</div>
<div class="store" style="left:673px;width:187px"><i></i>Desktop Store</div>

<!-- FAQ -->
<h2 class="abs center faq-title">FAQS</h2>
<div class="abs center eyebrow faq-sub">Ask any questions</div>
<div class="faq-item" style="top:4146px">1 Nam quibus rebus efficiuntur voluptates? <span class="plus">+</span></div>
<div class="faq-item" style="top:4216px">2 Huic mori optimum esse propter desperati ? <span class="plus">+</span></div>
<div class="faq-item" style="top:4285px">3 Est enim effectrix multarum et magnarum ? <span class="plus">+</span></div>
<div class="faq-item" style="top:4355px">4 Deque his rebus satis multa in nostris de ? <span class="plus">+</span></div>
<div class="abs faq-open">
  <div class="q"><span>Q: Loremipsum is simply dummy text?</span><span>–</span></div>
  <p class="a">Lorem ipsum dolor sit amet, consectetur adipiscing elit. Quid autem habent admirationis, cum prope accesseris? An hoc usque quaque, aliter in vita? Non igitur de improbo, sed de callido improbo quaerimus, qualis quaeque efficiuntur voluptates, eae non sunt in potestate sapientis. Negare non possum. Huic mori optimum esse propter desperationem sapientiae, illi propter spem vivere. Et quod est munus, quod opus sapientiae? Non modo carum sibi quemque, verum etiam vehementer carum esse? Tu enim ista lenius, hic stoicorum more nos vexat. Collatio igitur ista te nihil iuvat. Videamus animi partes, quarum est conspectus illustrior; sapientiae, illi propter spem vivere.</p>
</div>

<!-- Footer -->
<footer class="abs site-footer"></footer>
<div class="abs foot-brand"><span class="brand-dot"></span>Brisk Trail</div>
<p class="abs foot-about">Lorem ipsum dolor sit amet consectetur adipiscing elit. Quid autem habent admira sapientiae.</p>
<div class="abs socials"><i></i><i></i><i></i><i></i></div>

<div class="abs foot-h" style="left:378px;top:4566px">Contact info</div>
<div class="abs foot-col" style="left:378px;top:4616px">412 Harbor Bend Road<br>Fairhaven, Oregon 90210</div>
<div class="abs foot-col" style="left:378px;top:4672px"><b style="font-size:13px">555-014-7788</b><br>info@brisk-trail.example<br>www.brisk-trail-example.com</div>

<div class="abs foot-h" style="left:668px;top:4566px">Quick Link</div>
<ul class="abs quick-links"><li>About</li><li>Pricing</li><li>Blog</li><li>Support</li><li>Reviews</li><li>Contact Us</li><li>Free-Trial</li></ul>

<div class="abs foot-h" style="left:929px;top:4566px">Practice Areas</div>
<ul class="abs practice"><li>Personal Injury Claims</li><li>Medical Negligence</li><li>Professional Negligence</li><li>Commercial Litigation</li><li>Dispute Resolution</li><li style="border-bottom:none">Commercial Property</li></ul>

<div class="abs copyright">Copyright 2020, Northgate Counsel. All Right Reserved</div>

</body>
</html>
```